HL - business card

Harbor Lane Brokers is an insurance brokerage firm, inovative, proactive, vigorous, which aims to become the leader of the insurance brokers in Anfrica. We should like to get some designs which should be avoided also in Gray / Metallic for the Administration and Orange / Blue for the Managers (ike in the picture sent). The Blue / Green logo is not the correct one, but the source of the file. Please adjust the color accordingly for the business cards. 1 / Orange / Blue 2 / Gray / Metallic We want something classic but which is transmitted strenght, inovation, modernity and most of all, rapidity. We want something start-up like, very punchy and catching eye remaining profesional at the same time. Name: Tobias Wendell Function: Managing Director Address: N ° 17/18 Rua Dovel - R / C 2B Direita - Bairro Sambelo - Luanda Tel: (+244) 947 385 610 Email: tobias.wendell@harbor-l.com Website: www.harbor-l. com We want classic in the front and creative, colorfull at the back. The cards will be printed in relief, with very high quality of paper.
Insurance Broker
Designer to choose colors to be used in the design.

```html
<!DOCTYPE html>
<html lang="en">
<head>
<meta charset="utf-8">
<title>HL - business card</title>
<link rel="stylesheet" href="https://fonts.googleapis.com/css2?family=Exo+2:wght@500;600&family=Lato:wght@400&display=swap">
<style>
  :root {
    --brand-orange: #f26a21;
    --brand-blue: #29a8e0;
    --paper: #ffffff;
    --stage: #9c9c9c;
    --ink-light: #ffffff;
    --watermark: #f2f2f2;
  }
  * { box-sizing: border-box; margin: 0; padding: 0; }
  html, body {
    width: 1200px; height: 802px; overflow: hidden;
    background: var(--stage);
  }
  .canvas { position: relative; width: 1200px; height: 802px; }
  .card {
    position: absolute; top: 274px;
    width: 442px; height: 265px;
    overflow: hidden;
  }
  .card--front { left: 136px; background: var(--brand-orange); }
  .card--back { left: 624px; background: var(--paper); }
  .card__band { position: absolute; inset: 0; width: 442px; height: 265px; }
  .illustration {
    position: absolute;
    border-radius: 60px 60px 24px 24px;
    transform: rotate(45deg);
  }
  .illustration--front {
    left: 268px; top: -28px; width: 112px; height: 300px;
    background: linear-gradient(180deg, rgba(255,255,255,0.95), rgba(255,255,255,0.8));
  }
  .illustration--back {
    left: 88px; top: -35px; width: 112px; height: 300px;
    background: var(--watermark);
  }
  .contact {
    position: absolute; left: 17px; top: 36px;
    color: var(--ink-light);
    font-family: "Lato", sans-serif; font-size: 12.5px; line-height: 16px;
  }
  .contact__name {
    font-family: "Exo 2", sans-serif; font-weight: 500;
    font-size: 17px; line-height: 18px; letter-spacing: 0.2px;
    text-transform: uppercase;
  }
  .contact__role { margin-bottom: 16px; }
  .contact__line { display: flex; align-items: center; gap: 3px; }
  .contact__icon { width: 12px; height: 11px; flex: none; }
  .contact__address { margin-top: 14px; }
  .wordmark {
    position: absolute; left: 0; right: 0; top: 166px;
    display: flex; align-items: center; justify-content: center; gap: 8px;
  }
  .wordmark__dot {
    width: 14px; height: 14px; border-radius: 50%;
    background: var(--brand-orange);
  }
  .wordmark__name {
    font-family: "Exo 2", sans-serif; font-weight: 600;
    font-size: 21px; letter-spacing: 0.3px;
    color: var(--brand-blue); text-transform: uppercase;
  }
</style>
</head>
<body>
<main class="canvas">
  <section class="card card--front" aria-label="Card front">
    <svg class="card__band" viewBox="0 0 442 265" aria-hidden="true">
      <polygon points="180,265 442,34 442,265" fill="var(--brand-blue)"/>
    </svg>
    <div class="illustration illustration--front" role="img" aria-label="Large white rocket illustration launching diagonally across the card"></div>
    <div class="contact">
      <h1 class="contact__name">Tobias Wendell</h1>
      <p class="contact__role">Managing Director</p>
      <p class="contact__line">
        <svg class="contact__icon" viewBox="0 0 12 11" aria-hidden="true">
          <path d="M1 3.5 C1 1.5 11 1.5 11 3.5 L11 4.5 L8.5 4.5 L8.5 3.3 L3.5 3.3 L3.5 4.5 L1 4.5 Z" fill="currentColor"/>
          <path d="M2.5 5.5 L9.5 5.5 L11 10 L1 10 Z" fill="currentColor"/>
        </svg>
        (+244) 947 385 610
      </p>
      <p class="contact__line">
        <svg class="contact__icon" viewBox="0 0 12 11" aria-hidden="true">
          <rect x="1" y="2" width="10" height="7.5" fill="currentColor"/>
          <path d="M1.5 2.5 L6 6 L10.5 2.5" fill="none" stroke="var(--brand-orange)" stroke-width="1"/>
        </svg>
        tobias.wendell@harbor-l.com
      </p>
      <p class="contact__address">N ° 17/18 Rua Dovel - R / C<br>2B Direita<br>Bairro Sambelo - Luanda</p>
    </div>
  </section>

  <section class="card card--back" aria-label="Card back">
    <div class="illustration illustration--back" role="img" aria-label="Faint rocket watermark illustration"></div>
    <div class="wordmark">
      <span class="wordmark__dot" aria-hidden="true"></span>
      <span class="wordmark__name">Harbor Lane Brokers</span>
    </div>
  </section>
</main>
</body>
</html>
```